stationary for home builder
Birchwood Custom Homes, Inc.
Project: stationary for home builder
stationary for home builder - Real Estate
Creative Brief
Professional
Dale Morrow
President
4200 Tern Avenue, suite 310 Bayview Cove, CA 92777
bchdalemorrow@mailvista.test

```html
<!DOCTYPE html>
<html lang="en">
<head>
<meta charset="utf-8">
<title>Birchwood Custom Homes, Inc. – Business Card</title>
<link rel="stylesheet" href="https://fonts.googleapis.com/css2?family=Cinzel:wght@400;600;700&display=swap">
<style>
  :root {
    --stage: #8e9093;
    --frame: #6f7175;
    --frame-edge: #55575b;
    --paper: #ffffff;
    --brand-red: #c0282c;
    --band-red: #b3262a;
    --band-deep: #9d1f23;
    --stripe-dark: #2b2b2d;
    --silver: #d9d9dc;
    --ink-white: #ffffff;
  }
  * { margin: 0; padding: 0; box-sizing: border-box; }
  html, body { width: 1200px; height: 708px; overflow: hidden; }
  body {
    background: var(--stage);
    font-family: "Cinzel", serif;
    position: relative;
  }
  .card-frame {
    position: absolute;
    left: 140px; top: 92px;
    width: 920px; height: 516px;
    border-radius: 46px;
    background: var(--frame);
    border: 2px solid var(--frame-edge);
  }
  .card {
    position: absolute;
    left: 152px; top: 104px;
    width: 896px; height: 490px;
    border-radius: 36px;
    overflow: hidden;
    background: var(--paper);
  }
  .card__brand {
    position: absolute;
    left: 0; right: 0; top: 0; height: 256px;
    display: flex; align-items: center; justify-content: center;
    gap: 16px;
  }
  .brand-mark {
    width: 30px; height: 30px;
    background: var(--brand-red);
  }
  .brand-name {
    color: var(--brand-red);
    font-weight: 700;
    font-size: 34px;
    letter-spacing: 1px;
    line-height: 1;
  }
  .card__band {
    position: absolute;
    left: 0; right: 0; top: 256px; bottom: 0;
    background: linear-gradient(180deg, var(--band-red), var(--band-deep));
  }
  .band-rule {
    position: absolute; left: 0; right: 0; top: 0; height: 10px;
    background: var(--stripe-dark);
    border-bottom: 2px solid var(--silver);
  }
  .title-strip {
    position: absolute; left: 0; right: 0; top: 29px; height: 62px;
    background: linear-gradient(90deg, var(--band-deep), var(--brand-red) 50%, var(--band-deep));
    border-top: 2px solid var(--silver);
    border-bottom: 2px solid var(--silver);
    display: flex; align-items: center; justify-content: center;
    color: var(--ink-white);
    font-size: 22px;
  }
  .title-strip .person-name { font-weight: 700; }
  .title-strip .divider { margin: 0 12px; font-weight: 400; }
  .contact {
    position: absolute; left: 0; right: 0; height: 22px;
    display: flex; justify-content: center; align-items: center;
    gap: 18px;
    color: var(--ink-white);
    font-size: 17px;
  }
  .contact--first { top: 150px; }
  .contact--second { top: 183px; }
  .contact-item { display: flex; align-items: center; gap: 6px; white-space: nowrap; }
  .contact-icon { width: 19px; height: 19px; flex: none; }
</style>
</head>
<body>
  <div class="card-frame"></div>
  <div class="card">
    <div class="card__brand">
      <div class="brand-mark"></div>
      <div class="brand-name">Birchwood Custom Homes, Inc.</div>
    </div>
    <div class="card__band">
      <div class="band-rule"></div>
      <div class="title-strip">
        <span class="person-name">Dale Morrow</span>
        <span class="divider">|</span>
        <span class="person-title">President</span>
      </div>
      <div class="contact contact--first">
        <span class="contact-item">
          <svg class="contact-icon" viewBox="0 0 20 20" aria-hidden="true"><circle cx="10" cy="10" r="10" fill="#fff"/><path d="M5 10.5 10 6l5 4.5h-1.6V14H6.6v-3.5z" fill="#b3262a"/></svg>
          4200 Tern Avenue, suite 310 Bayview Cove, CA 92777
        </span>
        <span class="contact-item">
          <svg class="contact-icon" viewBox="0 0 20 20" aria-hidden="true"><circle cx="10" cy="10" r="10" fill="#fff"/><path d="M6.5 5h2l1 3-1.3 1a6 6 0 0 0 2.8 2.8l1-1.3 3 1v2a1.5 1.5 0 0 1-1.5 1.5A9 9 0 0 1 5 6.5 1.5 1.5 0 0 1 6.5 5z" fill="#b3262a"/></svg>
          949-555-0142
        </span>
      </div>
      <div class="contact contact--second">
        <span class="contact-item">
          <svg class="contact-icon" viewBox="0 0 20 20" aria-hidden="true"><circle cx="10" cy="10" r="10" fill="#fff"/><rect x="7" y="4.5" width="6" height="11" rx="1" fill="#b3262a"/><rect x="8" y="6" width="4" height="6.5" fill="#fff"/></svg>
          949-555-0187
        </span>
        <span class="contact-item">
          <svg class="contact-icon" viewBox="0 0 20 20" aria-hidden="true"><circle cx="10" cy="10" r="10" fill="#fff"/><rect x="5" y="6.5" width="10" height="7" fill="#b3262a"/><path d="M5 6.5l5 4 5-4" fill="none" stroke="#fff" stroke-width="1"/></svg>
          bchdalemorrow@mailvista.test
        </span>
        <span class="contact-item">
          <svg class="contact-icon" viewBox="0 0 20 20" aria-hidden="true"><circle cx="10" cy="10" r="10" fill="#fff"/><circle cx="10" cy="10" r="5.5" fill="none" stroke="#b3262a" stroke-width="1.3"/><ellipse cx="10" cy="10" rx="2.2" ry="5.5" fill="none" stroke="#b3262a" stroke-width="1.1"/><path d="M4.5 10h11" stroke="#b3262a" stroke-width="1.1"/></svg>
          www.birchwoodhomes.test
        </span>
      </div>
    </div>
  </div>
</body>
</html>
```